MS Word Template needed for a company specialized in network and security infrastructures

We need a new MS Word Template. <br/>Our activity is services in IT (network infrastructure and security). We usually use french language. <br/>The template must be nice and beautiful, and easy to use. If possible, try to use as less as possible text zones to simplify redaction tasks. And try to use "native" polices in MS Word. I attached sample documents for example. Please try to use the same colour codes.

Target Market(s)

Consulting in Network and security domain

Industry/Entity Type

It Service

Colors

Designer to choose colors to be used in the design.

Requirements
Must have
• - Nice design
• - Easy to use
• - very professional aspect
Nice to have
• - actual oxa cable partners logo
• - actual colour code

```html
<!DOCTYPE html>
<html lang="fr">
<head>
<meta charset="utf-8">
<title>Oxa Cable Partners – Word Template Pages</title>
<link rel="stylesheet" href="https://fonts.googleapis.com/css2?family=Montserrat:wght@300;400;600;700;800&display=swap">
<style>
  :root {
    --navy: #13304a;
    --navy-deep: #112a45;
    --teal: #2b9bb2;
    --teal-soft: #c8e8ee;
    --green: #6dbf8b;
    --green-soft: #d6eedb;
    --sage: #9fc7b4;
    --ink: #2d3b47;
    --rule: #c9d3da;
    --paper: #ffffff;
    --canvas: #f2f4f5;
  }
  * { box-sizing: border-box; margin: 0; padding: 0; }
  html, body { width: 1200px; height: 3000px; overflow: hidden; }
  body {
    background: var(--canvas);
    font-family: "Montserrat", sans-serif;
    color: var(--ink);
    position: relative;
  }
  .page {
    position: absolute;
    width: 520px;
    height: 736px;
    background: var(--paper);
    box-shadow: 0 6px 18px rgba(0,0,0,.16);
    overflow: hidden;
  }
  .page--cover   { left: 40px;  top: 276px; border: 6px solid var(--navy); }
  .page--toc     { left: 640px; top: 276px; }
  .page--content { left: 40px;  top: 1132px; }
  .page--bullets { left: 640px; top: 1132px; }
  .page--back    { left: 340px; top: 1988px;
    background: linear-gradient(160deg, #285a5e 0%, #1d4456 45%, var(--navy-deep) 100%); }

  .band { position: absolute; left: 0; top: 0; width: 100%; height: 15px; }
  .band--green-teal { background: linear-gradient(90deg, var(--green), var(--teal)); }
  .band--teal-green { background: linear-gradient(90deg, var(--teal), var(--green)); }

  /* brand name lockup */
  .brand { position: absolute; display: flex; align-items: center; gap: 8px;
    font-family: "Montserrat", sans-serif; font-weight: 600; color: var(--teal);
    text-transform: uppercase; letter-spacing: .04em; white-space: nowrap; }
  .brand__dot { border-radius: 50%; background: var(--teal); flex: none; }

  .footer { position: absolute; left: 18px; right: 52px; bottom: 24px; height: 12px; }
  .footer .brand { top: 0; font-size: 6px; gap: 4px; }
  .footer .brand__dot { width: 9px; height: 9px; }
  .footer__rule { position: absolute; left: 88px; right: 0; top: 6px; border-top: 1px solid var(--rule); }
  .footer--right .brand { right: 0; }
  .footer--right .footer__rule { left: 0; right: 92px; }
  .footer--right { left: 52px; right: 18px; }

  /* cover */
  .cover__art { position: absolute; left: 0; top: 0; width: 508px; height: 724px; }
  .cover__dots { position: absolute; left: 34px; top: 520px; display: flex; gap: 4px; }
  .cover__dots span { width: 9px; height: 9px; border-radius: 50%; }
  .cover__title { position: absolute; left: 32px; top: 540px; font-size: 38px; font-weight: 800;
    color: var(--navy); letter-spacing: .01em; }
  .cover__subtitle { position: absolute; left: 35px; top: 590px; font-size: 15px; font-weight: 400;
    color: var(--teal); }
  .cover .brand { left: 330px; top: 658px; font-size: 12px; }
  .cover .brand__dot { width: 40px; height: 40px; }

  /* contents */
  .toc__label { position: absolute; left: 33px; top: 42px; font-size: 11px; font-weight: 700;
    color: var(--green); font-variant: small-caps; letter-spacing: .04em; }
  .toc__list { position: absolute; left: 33px; top: 64px; right: 32px; list-style: none; }
  .toc__item { display: flex; align-items: baseline; height: 17.5px; font-size: 9.5px; }
  .toc__num { width: 30px; flex: none; }
  .toc__item--l2 .toc__num { margin-left: 30px; width: 35px; }
  .toc__item--l3 .toc__num { margin-left: 30px; width: 35px; color: #7d8890; }
  .toc__item--l3 .toc__text { color: #7d8890; }
  .toc__lead { flex: 1; border-bottom: 1px dotted #555; margin: 0 3px; transform: translateY(-2px); }
  .toc__item--l1 .toc__lead { border-bottom-style: solid; }
  .toc__page { font-weight: 600; }

  /* content page */
  .h1 { position: absolute; left: 32px; top: 46px; font-size: 17px; font-weight: 800; color: var(--navy); letter-spacing: .02em; }
  .h1-rule { position: absolute; left: 32px; right: 32px; top: 72px; border-top: 1.5px solid var(--teal); }
  .h2 { position: absolute; left: 32px; top: 96px; font-size: 15px; font-weight: 700; color: #2e4657; }
  .h3 { position: absolute; left: 32px; top: 140px; font-size: 9px; color: var(--teal); text-transform: uppercase; letter-spacing: .03em; }
  .h4 { position: absolute; left: 32px; top: 175px; font-size: 9px; color: var(--sage); text-transform: uppercase; letter-spacing: .03em; }
  .h5 { position: absolute; left: 32px; top: 210px; font-size: 8.5px; color: var(--ink); }
  .table-title { position: absolute; left: 32px; font-size: 15px; font-weight: 700; color: var(--navy); }
  .data-table { position: absolute; left: 32px; width: 456px; border-collapse: collapse; font-size: 8.5px; }
  .data-table caption { display: none; }
  .data-table th { color: #fff; font-weight: 700; text-align: left; height: 22px; padding: 0 5px; font-size: 8px; }
  .data-table td { height: 22px; padding: 0 5px; font-weight: 300; color: var(--ink); }
  .data-table col.c1 { width: 87px; } .data-table col.c2 { width: 81px; } .data-table col.c3 { width: 82px; }
  .data-table col.c4 { width: 80px; }
  .data-table--teal { top: 270px; border-top: 2px solid var(--teal); border-bottom: 1px solid var(--teal); }
  .data-table--teal th { background: var(--teal); }
  .data-table--teal tr.is-alt td { background: var(--teal-soft); border-top: 1px solid var(--teal); border-bottom: 1px solid var(--teal); }
  .data-table--green { top: 412px; border-top: 2px solid var(--teal); border-bottom: 1px solid var(--teal); }
  .data-table--green th { background: var(--green); }
  .data-table--green tr.is-alt td { background: var(--green-soft); border-top: 1px solid var(--green); border-bottom: 1px solid var(--green); }

  /* bullets page */
  .bullet-list { position: absolute; left: 30px; top: 38px; list-style: none; font-size: 8px; color: var(--teal); line-height: 17px; }
  .num-list { position: absolute; left: 46px; top: 150px; list-style: none; font-size: 8px; color: var(--ink); line-height: 14.5px; }
  .num-list > li { position: relative; padding-left: 16px; }
  .num-list > li::before { content: ""; position: absolute; left: 0; top: 5px; width: 6px; height: 6px; border-radius: 50%; background: var(--navy); }
  .num-list ul { list-style: none; padding-left: 48px; }
  .num-list ul li { position: relative; padding-left: 14px; }
  .num-list ul li::before { content: ""; position: absolute; left: 0; top: 6px; width: 3px; height: 3px; border-radius: 50%; background: var(--navy); }

  /* back cover */
  .page--back .brand { left: 50%; transform: translateX(-50%); bottom: 60px; font-size: 9px; color: #cfe3ea; gap: 6px; }
  .page--back .brand__dot { width: 28px; height: 28px; background: var(--teal); }
</style>
</head>
<body>

  <!-- Front cover -->
  <section class="page page--cover" aria-label="Couverture">
    <svg class="cover__art" viewBox="0 0 345 491" preserveAspectRatio="none">
      <defs>
        <linearGradient id="g-network" x1="0" y1="0" x2="1" y2="1">
          <stop offset="0" stop-color="#1f3f72"/>
          <stop offset=".45" stop-color="#3f79b6"/>
          <stop offset="1" stop-color="#132a4e"/>
        </linearGradient>
        <linearGradient id="g-tablet" x1="0" y1="0" x2="1" y2="1">
          <stop offset="0" stop-color="#d9e3ee"/>
          <stop offset=".5" stop-color="#5d7fa6"/>
          <stop offset="1" stop-color="#2a4d78"/>
        </linearGradient>
      </defs>
      <polygon role="img" aria-label="Photo : personne interagissant avec un réseau numérique d'icônes connectées"
        points="0,0 345,0 345,338 0,108" fill="url(#g-network)"/>
      <polygon role="img" aria-label="Photo : main utilisant une tablette avec graphiques"
        points="0,124 222,270 0,338" fill="url(#g-tablet)"/>
    </svg>
    <div class="cover__dots"><span style="background:var(--green)"></span><span style="background:var(--teal)"></span><span style="background:var(--navy)"></span></div>
    <h1 class="cover__title">TITLE HERE</h1>
    <p class="cover__subtitle">SUBTITLE HERE</p>
    <div class="brand"><span class="brand__dot"></span>Oxa Cable Partners</div>
  </section>

  <!-- Table of contents -->
  <section class="page page--toc" aria-label="Sommaire">
    <div class="band band--green-teal"></div>
    <h2 class="toc__label">Contents</h2>
    <ol class="toc__list">
      <li class="toc__item toc__item--l1"><span class="toc__num">1.</span><span class="toc__text">Heading 01</span><span class="toc__lead"></span><span class="toc__page">3</span></li>
      <li class="toc__item toc__item--l2"><span class="toc__num">1.1.</span><span class="toc__text">Heading 02</span><span class="toc__lead"></span><span class="toc__page">3</span></li>
      <li class="toc__item toc__item--l3"><span class="toc__num">1.1.1.</span><span class="toc__text">Heading 03</span><span class="toc__lead"></span><span class="toc__page">3</span></li>
      <li class="toc__item toc__item--l3"><span class="toc__num">1.1.2.</span><span class="toc__text">Heading 05</span><span class="toc__lead"></span><span class="toc__page">3</span></li>
    </ol>
    <footer class="footer"><div class="brand"><span class="brand__dot"></span>Oxa Cable Partners</div><div class="footer__rule"></div></footer>
  </section>

  <!-- Content page -->
  <section class="page page--content" aria-label="Page de contenu">
    <div class="band band--teal-green"></div>
    <h2 class="h1">HEADING 01</h2>
    <div class="h1-rule"></div>
    <h3 class="h2">Heading 02</h3>
    <h4 class="h3">Heading 03</h4>
    <h5 class="h4">Heading 04</h5>
    <h6 class="h5">Heading 05</h6>

    <p class="table-title" style="top:245px">Table 01</p>
    <table class="data-table data-table--teal">
      <colgroup><col class="c1"><col class="c2"><col class="c3"><col class="c4"><col></colgroup>
      <tr><th>Versão</th><th>Data</th><th>Autor</th><th>Comentários</th><th>Elaborado/modificado</th></tr>
      <tr><td>1.00</td><td>00</td><td>000</td><td>Original</td><td>000</td></tr>
      <tr class="is-alt"><td>2.00</td><td>000</td><td>00</td><td>Original</td><td>000</td></tr>
      <tr><td>000</td><td>000</td><td>000</td><td>000</td><td>000</td></tr>
    </table>

    <p class="table-title" style="top:387px">Table 02</p>
    <table class="data-table data-table--green">
      <colgroup><col class="c1"><col class="c2"><col class="c3"><col class="c4"><col></colgroup>
      <tr><th>Versão</th><th>Data</th><th>Autor</th><th>Comentários</th><th>Elaborado/modificado</th></tr>
      <tr><td>1.00</td><td></td><td></td><td>Original</td><td>000</td></tr>
      <tr class="is-alt"><td>2.00</td><td>000</td><td>00</td><td>Original</td><td>000</td></tr>
      <tr><td>000</td><td>000</td><td>000</td><td>000</td><td>000</td></tr>
    </table>
    <footer class="footer footer--right"><div class="footer__rule"></div><div class="brand"><span class="brand__dot"></span>Oxa Cable Partners</div></footer>
  </section>

  <!-- Bullets page -->
  <section class="page page--bullets" aria-label="Page de listes">
    <div class="band band--teal-green"></div>
    <ul class="bullet-list">
      <li>OCP Bullet 1</li><li>OCP Bullet 2</li><li>OCP Bullet 3</li><li>OCP Bullet 4</li><li>OCP Bullet 5</li>
    </ul>
    <ul class="num-list">
      <li>OCP Numbered Bullet 1<ul><li>OCP Numbered Bullet 1</li></ul></li>
      <li>OCP Numbered Bullet 1<ul><li>OCP Numbered Bullet 1</li></ul></li>
      <li>OCP Numbered Bullet 1<ul><li>OCP Numbered Bullet 1</li></ul></li>
    </ul>
    <footer class="footer"><div class="brand"><span class="brand__dot"></span>Oxa Cable Partners</div><div class="footer__rule"></div></footer>
  </section>

  <!-- Back cover -->
  <section class="page page--back" aria-label="Quatrième de couverture">
    <div class="brand"><span class="brand__dot"></span>Oxa Cable Partners</div>
  </section>

</body>
</html>
```